Funky new Serviced Apartment Company needs a website + logo

Bright Nest Serviced Accommodation is a new company aiming to attract customers who need temporary accommodation (2 days to 6 months) in city locations.

Our customers make considerable savings on longer stays compared to hotels, and have all the creature comforts of home including super-fast WIFI, comfy beds, full kitchen and modern, yet comfortable, furniture.

Another key feature of the design is a page to attract "Partners" who "Work with Us" by allowing us to manage their properties and becoming part of our network of accommodation units. I have include a brochure from one of our competitors, and a video can be found here: http://lnkvault-example.com/aptclip-7 - both can be used as I have permission.

The website design should work on all devices and screen sizes, and lend itself to a mobile app.

We would like to see website designs that are modern and simple, with a strong brand logo. The final design should communicate "Home From Home" and aim to attract professionals away from home on business for long periods of time.

Target Market(s)

Professional People working away from home for extended periods of time

Industry/Entity Type

Accommodation

Contact Information for Business Card

Name, Title, Phone Number, Email
Callum Fenwick, Owner, 07831 552907, callum.fenwick@brightnestsa-example.co.uk

Logo Text

Bright Nest Service Accommodation (Serviced Accommodation optional)

Coding

Coded - Design and coding required

Number of Pages Required

3 page

Font styles to use
Sans Serif

Requirements
Must have
• A 3 page website: Home, Partners, Contact Us
• Home page should have an area to list current apartment units, the user should be able to select a location and filter the list based on price and number of people.
• Partners page should inspire a "Work with us" call to action.
• The design should work with all screen sizes and devices.
• The design should say friendly and professional
Nice to have
• A simple logo, perhaps a smiling face made up using letters 'W' and 'H'.
• A neutral color scheme
Should not have
• No garish or vivid color scheme

```html
<!DOCTYPE html>
<html lang="en">
<head>
<meta charset="utf-8">
<title>Bright Nest – Serviced Apartments</title>
<link href="https://fonts.googleapis.com/css2?family=Roboto:wght@300;400;500;700&display=swap" rel="stylesheet">
<style>
:root{
  --ink:#222831;
  --text:#4a4f57;
  --muted:#8a9099;
  --line:#e6e8eb;
  --brand:#3aa0dc;
  --search:#5cb9e9;
  --accent:#f7a224;
  --tile:#f2f3f4;
  --footer:#3a3f4a;
  --footer-text:#8d939c;
  --white:#ffffff;
}
*{box-sizing:border-box;margin:0;padding:0}
html,body{width:1200px;height:3273px;overflow:hidden}
body{position:relative;background:var(--white);font-family:'Roboto',sans-serif;color:var(--text)}
.abs{position:absolute}

/* header */
.site-header{left:0;top:0;width:1200px;height:65px;background:var(--white)}
.brand{left:87px;top:18px;display:flex;align-items:center;gap:10px;font-weight:500;font-size:16px;color:var(--ink)}
.brand-dot{width:26px;height:26px;border-radius:50%;background:var(--brand)}
.main-nav{right:87px;top:24px;display:flex;align-items:center;gap:34px;font-size:12px;color:var(--ink)}
.main-nav .active{color:var(--brand);display:flex;align-items:center;gap:6px}

/* hero */
.hero{left:0;top:65px;width:1200px;height:505px;background:linear-gradient(100deg,#6d6e70 0%,#9a9a98 25%,#cfcfcc 50%,#b9b8b4 72%,#8d8c89 100%)}
.hero-kicker{left:90px;top:212px;color:var(--white);font-size:16px}
.hero-title{left:88px;top:236px;color:var(--white);font-size:37px;font-weight:400}
.hero-btn{left:91px;top:293px;width:139px;height:30px;background:var(--accent);color:var(--white);font-size:10px;font-weight:500;display:flex;align-items:center;justify-content:center;text-transform:uppercase}
.hero-arrow{top:245px;width:24px;height:64px;background:rgba(60,60,60,.55);display:flex;align-items:center;justify-content:center}
.mouse{left:589px;top:440px;width:22px;height:34px;border:2px solid var(--white);border-radius:11px}
.mouse::after{content:"";position:absolute;left:8px;top:7px;width:2px;height:7px;background:var(--white);border-radius:1px}

/* search */
.search{left:87px;top:641px;width:1024px;height:86px;background:var(--search);display:flex;align-items:center;padding-left:61px;gap:8px}
.field{height:40px;background:var(--white);border-radius:2px;font-size:10px;color:var(--muted);display:flex;align-items:center;justify-content:space-between;padding:0 12px 0 16px}
.check-btn{width:166px;height:40px;background:var(--accent);color:var(--white);font-size:10px;font-weight:500;display:flex;align-items:center;justify-content:center;text-transform:uppercase}

/* section titles */
.section-title{left:0;width:1200px;text-align:center;font-size:30px;font-weight:400;color:var(--ink)}

/* cards */
.grid{left:89px;width:1022px;display:grid;grid-template-columns:repeat(3,332px);column-gap:13px}
.room-card{height:413px;border:1px solid var(--line);background:var(--white);margin-bottom:15px}
.card-photo{height:230px}
.card-body{padding:31px 30px 0 30px}
.card-title{font-size:15px;color:var(--ink);font-weight:400}
.card-loc{margin-top:6px;font-size:11px;color:var(--text);display:flex;align-items:center;gap:6px}
.card-stats{margin-top:20px;padding-top:14px;border-top:1px solid var(--line);display:flex;gap:22px;font-size:10px;color:var(--muted)}
.card-stats span{display:flex;align-items:center;gap:5px}
.card-foot{margin-top:18px;display:flex;justify-content:space-between;align-items:center}
.price{font-size:19px;font-weight:700;color:var(--ink)}
.card-actions{display:flex;gap:10px}

/* cta band */
.rent-band{left:0;top:1772px;width:1200px;height:183px;background:linear-gradient(90deg,#4b5565 0%,#5f6878 45%,#6c7584 100%)}
.rent-title{left:87px;top:64px;font-size:27px;color:var(--white);font-weight:400}
.rent-sub{left:89px;top:100px;font-size:14px;color:var(--white)}
.rent-btn{left:945px;top:78px;width:165px;height:40px;background:var(--accent);color:var(--white);font-size:10px;font-weight:500;display:flex;align-items:center;justify-content:center;text-transform:uppercase}

/* partners */
.partners-lead{left:330px;top:2079px;width:540px;text-align:center;font-size:12px;line-height:19px;color:var(--ink)}
.partner-row{left:87px;top:2145px;width:1024px;height:168px;display:grid;grid-template-columns:repeat(6,1fr)}
.partner-tile{display:flex;align-items:center;justify-content:center}
.partner-tile:nth-child(even){background:var(--tile)}
.badge{width:92px;height:92px;border:3px solid #3c3f44;border-radius:4px}
.partner-tile:nth-child(2) .badge{border-radius:50%}

/* blog */
.blog-card{height:383px;border:1px solid var(--line);background:var(--white)}
.blog-meta{font-size:10px;color:var(--text);display:flex;gap:12px}
.blog-title{margin-top:14px;font-size:15px;line-height:22px;font-weight:400;color:var(--ink)}
.blog-counts{margin-top:16px;display:flex;gap:14px;font-size:10px;color:var(--muted)}
.blog-counts span{display:flex;align-items:center;gap:4px}

/* footer */
.site-footer{left:0;top:2905px;width:1200px;height:368px;background:var(--footer)}
.foot-label{font-size:11px;font-weight:500;color:var(--white);text-transform:uppercase}
.gallery{left:98px;top:80px;display:grid;grid-template-columns:repeat(4,68px);gap:6px}
.gallery div{height:64px}
.touch-list{left:445px;top:110px;width:210px;font-size:11px;line-height:22px;color:var(--footer-text)}
.touch-list li{list-style:none;display:flex;gap:12px;margin-bottom:14px}
.foot-brand{left:780px;top:60px;display:flex;align-items:center;gap:10px;color:var(--white);font-size:15px;font-weight:500}
.foot-about{left:780px;top:110px;width:330px;font-size:11px;line-height:22px;color:var(--footer-text)}
.foot-rule{left:87px;top:322px;width:1024px;height:1px;background:#4c525d}
.copyright{left:0;top:341px;width:1200px;text-align:center;font-size:11px;color:var(--footer-text)}
</style>
</head>
<body>

<header class="site-header abs">
  <div class="brand abs"><span class="brand-dot"></span>Bright Nest</div>
  <nav class="main-nav abs">
    <span class="active"><svg width="11" height="10" viewBox="0 0 11 10"><path d="M1 5L5.5 1 10 5V9H1Z" fill="#3aa0dc"/></svg>Home</span>
    <span>Partners</span>
    <span>Contact Us</span>
    <svg width="16" height="12" viewBox="0 0 16 12"><path d="M0 1H16M0 6H16M0 11H16" stroke="#222831" stroke-width="1.6"/></svg>
  </nav>
</header>

<section class="hero abs" role="img" aria-label="Bright bedroom with a patterned bed, lamp and curtained window">
  <p class="hero-kicker abs">Good Service is our passion</p>
  <h1 class="hero-title abs">Awesome Apartment</h1>
  <a class="hero-btn abs">Special Offer</a>
  <div class="hero-arrow abs" style="left:0"><svg width="8" height="10" viewBox="0 0 8 10"><path d="M6 1L2 5 6 9" stroke="#fff" fill="none" stroke-width="1.5"/></svg></div>
  <div class="hero-arrow abs" style="right:0"><svg width="8" height="10" viewBox="0 0 8 10"><path d="M2 1L6 5 2 9" stroke="#fff" fill="none" stroke-width="1.5"/></svg></div>
  <div class="mouse abs"></div>
</section>

<form class="search abs">
  <div class="field" style="width:202px">Arrival Date<svg width="12" height="11" viewBox="0 0 12 11"><rect x="1" y="2" width="10" height="8" fill="none" stroke="#666"/><path d="M1 4.5H11" stroke="#666"/></svg></div>
  <div class="field" style="width:202px">Departure Date<svg width="12" height="11" viewBox="0 0 12 11"><rect x="1" y="2" width="10" height="8" fill="none" stroke="#666"/><path d="M1 4.5H11" stroke="#666"/></svg></div>
  <div class="field" style="width:150px">Adults<svg width="6" height="10" viewBox="0 0 6 10"><path d="M0 4L3 1 6 4M0 6L3 9 6 6" fill="#666"/></svg></div>
  <div class="field" style="width:150px">Children<svg width="6" height="10" viewBox="0 0 6 10"><path d="M0 4L3 1 6 4M0 6L3 9 6 6" fill="#666"/></svg></div>
  <a class="check-btn">Check Availability</a>
</form>

<h2 class="section-title abs" style="top:776px">Rooms &amp; Apartments</h2>

<div class="grid abs" style="top:840px">
  <article class="room-card"><div class="card-photo" role="img" aria-label="Bedroom with wood panelled wall and warm lighting" style="background:linear-gradient(160deg,#d9c3a8,#8a5e3c 60%,#5b3a26)"></div>
    <div class="card-body"><h3 class="card-title">Family Apartment</h3><p class="card-loc"><svg width="8" height="11" viewBox="0 0 8 11"><path d="M4 11C1 7 0 5.5 0 4a4 4 0 018 0c0 1.5-1 3-4 7z" fill="#333"/><circle cx="4" cy="4" r="1.4" fill="#fff"/></svg>Harbour Row, Norhaven</p>
    <div class="card-stats"><span><svg width="12" height="8" viewBox="0 0 12 8"><path d="M0 0V8M0 6H12V8M3 4H12V6" stroke="#999" fill="none"/></svg>3 Bedrooms</span><span><svg width="11" height="9" viewBox="0 0 11 9"><path d="M0 4H11V6C11 8 9 8 8 8H3C2 8 0 8 0 6Z M2 4V1H4" fill="#999"/></svg>2 Bathroom</span><span><svg width="9" height="10" viewBox="0 0 9 10"><circle cx="4.5" cy="2.5" r="2.3" fill="#999"/><path d="M0 10C0 6 9 6 9 10Z" fill="#999"/></svg>6 Adult</span></div>
    <div class="card-foot"><span class="price">$200</span><span class="card-actions"><svg width="11" height="11" viewBox="0 0 11 11"><circle cx="2" cy="5.5" r="1.8" fill="#555"/><circle cx="9" cy="2" r="1.8" fill="#555"/><circle cx="9" cy="9" r="1.8" fill="#555"/><path d="M2 5.5L9 2M2 5.5L9 9" stroke="#555"/></svg><svg width="11" height="11" viewBox="0 0 11 11"><path d="M5.5 .8L7 4H10.4L7.7 6.2 8.7 9.9 5.5 7.8 2.3 9.9 3.3 6.2 .6 4H4Z" fill="none" stroke="#555"/></svg></span></div></div></article>
  <article class="room-card"><div class="card-photo" role="img" aria-label="Open living room with white sofa and purple ceiling light" style="background:linear-gradient(160deg,#b8acd0,#d8d6da 45%,#7d7b80)"></div>
    <div class="card-body"><h3 class="card-title">Family Apartment</h3><p class="card-loc"><svg width="8" height="11" viewBox="0 0 8 11"><path d="M4 11C1 7 0 5.5 0 4a4 4 0 018 0c0 1.5-1 3-4 7z" fill="#333"/><circle cx="4" cy="4" r="1.4" fill="#fff"/></svg>Harbour Row, Norhaven</p>
    <div class="card-stats"><span><svg width="12" height="8" viewBox="0 0 12 8"><path d="M0 0V8M0 6H12V8M3 4H12V6" stroke="#999" fill="none"/></svg>3 Bedrooms</span><span><svg width="11" height="9" viewBox="0 0 11 9"><path d="M0 4H11V6C11 8 9 8 8 8H3C2 8 0 8 0 6Z M2 4V1H4" fill="#999"/></svg>2 Bathroom</span><span><svg width="9" height="10" viewBox="0 0 9 10"><circle cx="4.5" cy="2.5" r="2.3" fill="#999"/><path d="M0 10C0 6 9 6 9 10Z" fill="#999"/></svg>6 Adult</span></div>
    <div class="card-foot"><span class="price">$200</span><span class="card-actions"><svg width="11" height="11" viewBox="0 0 11 11"><circle cx="2" cy="5.5" r="1.8" fill="#555"/><circle cx="9" cy="2" r="1.8" fill="#555"/><circle cx="9" cy="9" r="1.8" fill="#555"/><path d="M2 5.5L9 2M2 5.5L9 9" stroke="#555"/></svg><svg width="11" height="11" viewBox="0 0 11 11"><path d="M5.5 .8L7 4H10.4L7.7 6.2 8.7 9.9 5.5 7.8 2.3 9.9 3.3 6.2 .6 4H4Z" fill="none" stroke="#555"/></svg></span></div></div></article>
  <article class="room-card"><div class="card-photo" role="img" aria-label="Hotel style bedroom with grey walls and curtains" style="background:linear-gradient(160deg,#8e8f95,#5d5f68 55%,#3f414a)"></div>
    <div class="card-body"><h3 class="card-title">Family Apartment</h3><p class="card-loc"><svg width="8" height="11" viewBox="0 0 8 11"><path d="M4 11C1 7 0 5.5 0 4a4 4 0 018 0c0 1.5-1 3-4 7z" fill="#333"/><circle cx="4" cy="4" r="1.4" fill="#fff"/></svg>Harbour Row, Norhaven</p>
    <div class="card-stats"><span><svg width="12" height="8" viewBox="0 0 12 8"><path d="M0 0V8M0 6H12V8M3 4H12V6" stroke="#999" fill="none"/></svg>3 Bedrooms</span><span><svg width="11" height="9" viewBox="0 0 11 9"><path d="M0 4H11V6C11 8 9 8 8 8H3C2 8 0 8 0 6Z M2 4V1H4" fill="#999"/></svg>2 Bathroom</span><span><svg width="9" height="10" viewBox="0 0 9 10"><circle cx="4.5" cy="2.5" r="2.3" fill="#999"/><path d="M0 10C0 6 9 6 9 10Z" fill="#999"/></svg>6 Adult</span></div>
    <div class="card-foot"><span class="price">$200</span><span class="card-actions"><svg width="11" height="11" viewBox="0 0 11 11"><circle cx="2" cy="5.5" r="1.8" fill="#555"/><circle cx="9" cy="2" r="1.8" fill="#555"/><circle cx="9" cy="9" r="1.8" fill="#555"/><path d="M2 5.5L9 2M2 5.5L9 9" stroke="#555"/></svg><svg width="11" height="11" viewBox="0 0 11 11"><path d="M5.5 .8L7 4H10.4L7.7 6.2 8.7 9.9 5.5 7.8 2.3 9.9 3.3 6.2 .6 4H4Z" fill="none" stroke="#555"/></svg></span></div></div></article>
  <article class="room-card"><div class="card-photo" role="img" aria-label="Cream leather sofa in a warm lounge" style="background:linear-gradient(160deg,#a0522d,#6b3a24 40%,#d8cfc2 70%,#3b2a22)"></div>
    <div class="card-body"><h3 class="card-title">Family Apartment</h3><p class="card-loc"><svg width="8" height="11" viewBox="0 0 8 11"><path d="M4 11C1 7 0 5.5 0 4a4 4 0 018 0c0 1.5-1 3-4 7z" fill="#333"/><circle cx="4" cy="4" r="1.4" fill="#fff"/></svg>Harbour Row, Norhaven</p>
    <div class="card-stats"><span><svg width="12" height="8" viewBox="0 0 12 8"><path d="M0 0V8M0 6H12V8M3 4H12V6" stroke="#999" fill="none"/></svg>3 Bedrooms</span><span><svg width="11" height="9" viewBox="0 0 11 9"><path d="M0 4H11V6C11 8 9 8 8 8H3C2 8 0 8 0 6Z M2 4V1H4" fill="#999"/></svg>2 Bathroom</span><span><svg width="9" height="10" viewBox="0 0 9 10"><circle cx="4.5" cy="2.5" r="2.3" fill="#999"/><path d="M0 10C0 6 9 6 9 10Z" fill="#999"/></svg>6 Adult</span></div>
    <div class="card-foot"><span class="price">$200</span><span class="card-actions"><svg width="11" height="11" viewBox="0 0 11 11"><circle cx="2" cy="5.5" r="1.8" fill="#555"/><circle cx="9" cy="2" r="1.8" fill="#555"/><circle cx="9" cy="9" r="1.8" fill="#555"/><path d="M2 5.5L9 2M2 5.5L9 9" stroke="#555"/></svg><svg width="11" height="11" viewBox="0 0 11 11"><path d="M5.5 .8L7 4H10.4L7.7 6.2 8.7 9.9 5.5 7.8 2.3 9.9 3.3 6.2 .6 4H4Z" fill="none" stroke="#555"/></svg></span></div></div></article>
  <article class="room-card"><div class="card-photo" role="img" aria-label="Sunny sitting room with yellow striped armchairs" style="background:linear-gradient(160deg,#e9e3d2,#c9a24a 50%,#8a3a1e)"></div>
    <div class="card-body"><h3 class="card-title">Family Apartment</h3><p class="card-loc"><svg width="8" height="11" viewBox="0 0 8 11"><path d="M4 11C1 7 0 5.5 0 4a4 4 0 018 0c0 1.5-1 3-4 7z" fill="#333"/><circle cx="4" cy="4" r="1.4" fill="#fff"/></svg>Harbour Row, Norhaven</p>
    <div class="card-stats"><span><svg width="12" height="8" viewBox="0 0 12 8"><path d="M0 0V8M0 6H12V8M3 4H12V6" stroke="#999" fill="none"/></svg>3 Bedrooms</span><span><svg width="11" height="9" viewBox="0 0 11 9"><path d="M0 4H11V6C11 8 9 8 8 8H3C2 8 0 8 0 6Z M2 4V1H4" fill="#999"/></svg>2 Bathroom</span><span><svg width="9" height="10" viewBox="0 0 9 10"><circle cx="4.5" cy="2.5" r="2.3" fill="#999"/><path d="M0 10C0 6 9 6 9 10Z" fill="#999"/></svg>6 Adult</span></div>
    <div class="card-foot"><span class="price">$200</span><span class="card-actions"><svg width="11" height="11" viewBox="0 0 11 11"><circle cx="2" cy="5.5" r="1.8" fill="#555"/><circle cx="9" cy="2" r="1.8" fill="#555"/><circle cx="9" cy="9" r="1.8" fill="#555"/><path d="M2 5.5L9 2M2 5.5L9 9" stroke="#555"/></svg><svg width="11" height="11" viewBox="0 0 11 11"><path d="M5.5 .8L7 4H10.4L7.7 6.2 8.7 9.9 5.5 7.8 2.3 9.9 3.3 6.2 .6 4H4Z" fill="none" stroke="#555"/></svg></span></div></div></article>
  <article class="room-card"><div class="card-photo" role="img" aria-label="Bright bedroom with white bedding and window seating" style="background:linear-gradient(160deg,#eeeae2,#cfc6b6 50%,#7c7264)"></div>
    <div class="card-body"><h3 class="card-title">Family Apartment</h3><p class="card-loc"><svg width="8" height="11" viewBox="0 0 8 11"><path d="M4 11C1 7 0 5.5 0 4a4 4 0 018 0c0 1.5-1 3-4 7z" fill="#333"/><circle cx="4" cy="4" r="1.4" fill="#fff"/></svg>Harbour Row, Norhaven</p>
    <div class="card-stats"><span><svg width="12" height="8" viewBox="0 0 12 8"><path d="M0 0V8M0 6H12V8M3 4H12V6" stroke="#999" fill="none"/></svg>3 Bedrooms</span><span><svg width="11" height="9" viewBox="0 0 11 9"><path d="M0 4H11V6C11 8 9 8 8 8H3C2 8 0 8 0 6Z M2 4V1H4" fill="#999"/></svg>2 Bathroom</span><span><svg width="9" height="10" viewBox="0 0 9 10"><circle cx="4.5" cy="2.5" r="2.3" fill="#999"/><path d="M0 10C0 6 9 6 9 10Z" fill="#999"/></svg>6 Adult</span></div>
    <div class="card-foot"><span class="price">$200</span><span class="card-actions"><svg width="11" height="11" viewBox="0 0 11 11"><circle cx="2" cy="5.5" r="1.8" fill="#555"/><circle cx="9" cy="2" r="1.8" fill="#555"/><circle cx="9" cy="9" r="1.8" fill="#555"/><path d="M2 5.5L9 2M2 5.5L9 9" stroke="#555"/></svg><svg width="11" height="11" viewBox="0 0 11 11"><path d="M5.5 .8L7 4H10.4L7.7 6.2 8.7 9.9 5.5 7.8 2.3 9.9 3.3 6.2 .6 4H4Z" fill="none" stroke="#555"/></svg></span></div></div></article>
</div>

<section class="rent-band abs" role="img" aria-label="Dimmed hotel bedroom with twin beds behind the call to action">
  <h2 class="rent-title abs">Do you want to Rent your House</h2>
  <p class="rent-sub abs">Call us and list your property here</p>
  <a class="rent-btn abs">Contact Us</a>
</section>

<h2 class="section-title abs" style="top:2033px">Our Partners</h2>
<p class="partners-lead abs">Trusted owners and agents across the city work with us to offer calm,<br>well kept homes for longer stays.</p>
<div class="partner-row abs">
  <div class="partner-tile"><span class="badge"></span></div>
  <div class="partner-tile"><span class="badge"></span></div>
  <div class="partner-tile"><span class="badge"></span></div>
  <div class="partner-tile"><span class="badge"></span></div>
  <div class="partner-tile"><span class="badge"></span></div>
  <div class="partner-tile"><span class="badge"></span></div>
</div>

<h2 class="section-title abs" style="top:2375px">Our Blog</h2>
<div class="grid abs" style="top:2440px">
  <article class="blog-card"><div class="card-photo" role="img" aria-label="Loft room with timber beams and a daybed" style="background:linear-gradient(160deg,#f1efe9,#b7b29f 50%,#5d4230)"></div>
    <div class="card-body"><p class="blog-meta"><span>July 25, 2016</span><span>|</span><span>Rooms &amp; suites</span></p><h3 class="blog-title">Finding best places to visit in<br>California</h3>
    <p class="blog-counts"><span><svg width="11" height="7" viewBox="0 0 11 7"><path d="M0 3.5C3 -1 8 -1 11 3.5 8 8 3 8 0 3.5Z" fill="#666"/><circle cx="5.5" cy="3.5" r="1.5" fill="#fff"/></svg>35</span><span><svg width="10" height="9" viewBox="0 0 10 9"><path d="M5 8.5L1 4.5A2.3 2.3 0 015 1.5 2.3 2.3 0 019 4.5Z" fill="none" stroke="#3aa0dc"/></svg>09</span><span><svg width="11" height="9" viewBox="0 0 11 9"><path d="M1 1H10V6H4L1 8.5Z" fill="#5cb85c"/></svg>05</span></p></div></article>
  <article class="blog-card"><div class="card-photo" role="img" aria-label="Living room with fireplace, TV and red sofa" style="background:linear-gradient(160deg,#e9e7e3,#9b9791 50%,#8a4a3e)"></div>
    <div class="card-body"><p class="blog-meta"><span>July 25, 2016</span><span>|</span><span>Rooms &amp; suites</span></p><h3 class="blog-title">Finding best places to visit in<br>California</h3>
    <p class="blog-counts"><span><svg width="11" height="7" viewBox="0 0 11 7"><path d="M0 3.5C3 -1 8 -1 11 3.5 8 8 3 8 0 3.5Z" fill="#666"/><circle cx="5.5" cy="3.5" r="1.5" fill="#fff"/></svg>35</span><span><svg width="10" height="9" viewBox="0 0 10 9"><path d="M5 8.5L1 4.5A2.3 2.3 0 015 1.5 2.3 2.3 0 019 4.5Z" fill="none" stroke="#3aa0dc"/></svg>09</span><span><svg width="11" height="9" viewBox="0 0 11 9"><path d="M1 1H10V6H4L1 8.5Z" fill="#5cb85c"/></svg>05</span></p></div></article>
  <article class="blog-card"><div class="card-photo" role="img" aria-label="Bedroom with framed pictures above a dark headboard" style="background:linear-gradient(160deg,#8b7a63,#c9b9a0 50%,#4c3c2c)"></div>
    <div class="card-body"><p class="blog-meta"><span>July 25, 2016</span><span>|</span><span>Rooms &amp; suites</span></p><h3 class="blog-title">Finding best places to visit in<br>California</h3>
    <p class="blog-counts"><span><svg width="11" height="7" viewBox="0 0 11 7"><path d="M0 3.5C3 -1 8 -1 11 3.5 8 8 3 8 0 3.5Z" fill="#666"/><circle cx="5.5" cy="3.5" r="1.5" fill="#fff"/></svg>35</span><span><svg width="10" height="9" viewBox="0 0 10 9"><path d="M5 8.5L1 4.5A2.3 2.3 0 015 1.5 2.3 2.3 0 019 4.5Z" fill="none" stroke="#3aa0dc"/></svg>09</span><span><svg width="11" height="9" viewBox="0 0 11 9"><path d="M1 1H10V6H4L1 8.5Z" fill="#5cb85c"/></svg>05</span></p></div></article>
</div>

<footer class="site-footer abs">
  <h4 class="foot-label abs" style="left:89px;top:65px">Gallery</h4>
  <div class="gallery abs">
    <div role="img" aria-label="Gallery photo: sunset street" style="background:linear-gradient(#e08a2a,#6b4a2a)"></div>
    <div role="img" aria-label="Gallery photo: house front" style="background:linear-gradient(#9a8d7a,#5a4f42)"></div>
    <div role="img" aria-label="Gallery photo: colourful buildings" style="background:linear-gradient(#3b6fb0,#c0603a)"></div>
    <div role="img" aria-label="Gallery photo: city towers" style="background:linear-gradient(#9fb8cf,#4c5c6c)"></div>
    <div role="img" aria-label="Gallery photo: modern villa" style="background:linear-gradient(#c4ccd4,#7e8a94)"></div>
    <div role="img" aria-label="Gallery photo: white apartment block" style="background:linear-gradient(#e5e5e5,#5e6a76)"></div>
    <div role="img" aria-label="Gallery photo: evening house lights" style="background:linear-gradient(#23344f,#d08a3a)"></div>
    <div role="img" aria-label="Gallery photo: poolside resort" style="background:linear-gradient(#5aa6d8,#d8a060)"></div>
  </div>
  <h4 class="foot-label abs" style="left:445px;top:65px">Stay in touch</h4>
  <ul class="touch-list abs">
    <li><svg width="9" height="12" viewBox="0 0 9 12" style="margin-top:5px;flex:none"><path d="M4.5 12C1 7.5 0 6 0 4.5a4.5 4.5 0 019 0c0 1.5-1 3-4.5 7.5z" fill="none" stroke="#8d939c"/></svg><span>14 Harbour Row, Norhaven, open daily for guest support</span></li>
    <li><svg width="10" height="12" viewBox="0 0 10 12" style="margin-top:5px;flex:none"><rect x="1" y=".5" width="8" height="11" rx="1" fill="none" stroke="#8d939c"/></svg><span>+44 1632 960 418</span></li>
    <li><svg width="12" height="9" viewBox="0 0 12 9" style="margin-top:7px;flex:none"><rect x=".5" y=".5" width="11" height="8" fill="none" stroke="#8d939c"/><path d="M.5 .5L6 5 11.5 .5" fill="none" stroke="#8d939c"/></svg><span>info@brightnest-example.com</span></li>
  </ul>
  <div class="foot-brand abs"><span class="brand-dot"></span>Bright Nest</div>
  <p class="foot-about abs">Serviced homes for professionals on longer stays, with fast wifi, full kitchens and comfy beds in every unit across the city.</p>
  <div class="foot-rule abs"></div>
  <p class="copyright abs">Copyright 2017 Bright Nest, All Right Reserved</p>
</footer>

</body>
</html>
```